Homeowners Marketing Leads website design

I need a new website designed using the our attached company logo. We sale New Movers lists to businesses that need to sale/market their services/products to homeowners, they use our list to call or mail those customers about doing business with them.
Our 3 Steps process is;
1. (Our Clients) Receive leads of the most recent New Movers in their area.
2. (Our Clients) Do direct marketing of their company's services/products to those New Movers.
3. If (Our Clients) feel these leads/lists are not fresh and accurate, then (Our Clients) have no obligation to pay us. The leads are FREE.

These are examples of the types of companies that would look for our website to be able get leads/list from us through our website;
-Carpeting/Flooring
-Residential Landscaping
-Heat/Air Conditioning Services
-Painting
-Home Remodeling
-Windows Replacement
-Plumbing
-Pest Control
-Home Security Systems
-Appliances
-Furniture
-Home Theater/TV Mounting
-Mattress
Etc.

Target Market(s)

We sell lead lists to companies looking to do a mailing or cold-calling campaign to Residential New Movers (Homeowners)

Number of Pages Required

2 page

Requirements
Must have
• Contact Form so that our clients can enter the following;
• Name
• (Their) Business Name
• Email to Receive Lead
• Industry (This input will be a drop-down on the form)
• Comments/Questions (Box)
• (Submit Button)

```html
<!DOCTYPE html>
<html lang="en">
<head>
<meta charset="utf-8">
<title>Lead Harbor – New Movers Leads</title>
<link href="https://fonts.googleapis.com/css2?family=Roboto:wght@300;400;500;700&family=Roboto+Condensed:wght@400;700&display=swap" rel="stylesheet">
<style>
:root{
  --orange:#f47b20;
  --orange-dark:#d9650f;
  --ink:#333333;
  --muted:#777777;
  --light:#f1f1f1;
  --nav:#262626;
  --footer:#222222;
  --footer-bottom:#161616;
  --white:#ffffff;
}
*{box-sizing:border-box;margin:0;padding:0}
html,body{width:1200px;height:3024px;overflow:hidden}
body{font-family:"Roboto",sans-serif;color:var(--ink);background:var(--white);position:relative}
a{color:inherit;text-decoration:none}

/* header */
.site-header{height:128px;display:flex;justify-content:space-between;align-items:center;padding:0 88px;background:var(--white)}
.brand{display:flex;align-items:center;gap:14px}
.brand-mark{width:40px;height:40px;background:var(--orange)}
.brand-name{font-size:34px;font-weight:500;color:var(--orange)}
.header-right{display:flex;align-items:center;gap:22px}
.social-row{display:flex;gap:8px}
.social-row span{width:26px;height:26px;background:var(--orange);display:block}
.contact-lines{font-size:20px;line-height:28px;color:var(--ink)}
.contact-lines .phone{font-weight:700;font-size:24px}

/* hero */
.hero{position:relative;height:584px;background:linear-gradient(180deg,#6c7a86 0%,#8a8172 45%,#4b4a3e 75%,#2b2d26 100%)}
.main-nav{position:absolute;left:88px;right:88px;top:0;height:52px;background:var(--nav);display:flex;align-items:center}
.main-nav a{color:var(--white);font-size:15px;text-transform:uppercase;padding:0 32px;line-height:52px}
.main-nav a.active{background:#111}
.main-nav a.orange{background:var(--orange)}
.nav-search{margin-left:auto;margin-right:12px;width:180px;height:32px;background:var(--white);display:flex;align-items:center;justify-content:space-between;padding:0 10px;font-size:14px;color:#999}
.hero-content{position:absolute;left:0;right:0;top:200px;text-align:center;color:var(--white)}
.hero-mark{width:96px;height:60px;margin:0 auto 14px;border:4px solid var(--white)}
.hero-title{font-family:"Roboto Condensed",sans-serif;font-size:52px;font-weight:700;letter-spacing:2px}
.hero-sub{font-family:"Roboto Condensed",sans-serif;font-size:28px;margin-top:8px}
.hero-dots{position:absolute;bottom:30px;left:0;right:0;display:flex;justify-content:center;gap:8px}
.hero-dots span{width:10px;height:10px;border-radius:50%;background:rgba(255,255,255,.55)}
.hero-dots span.on{background:var(--white)}

/* process */
.process{height:420px;background:var(--light);text-align:center;padding-top:76px}
.section-title{font-family:"Roboto Condensed",sans-serif;font-size:32px;font-weight:700;text-transform:uppercase;color:var(--ink)}
.section-title em{font-style:normal;color:var(--orange)}
.steps{display:flex;justify-content:center;align-items:flex-start;margin-top:50px}
.step{width:240px}
.step-icon{width:92px;height:92px;border-radius:50%;background:var(--white);margin:0 auto;display:flex;align-items:center;justify-content:center;box-shadow:0 2px 6px rgba(0,0,0,.08)}
.step h3{font-size:16px;font-weight:500;margin-top:18px}
.step p{font-size:13px;color:var(--muted);margin:8px auto 0;width:200px;line-height:18px}
.step-arrow{width:120px;padding-top:34px;display:flex;justify-content:center}

/* welcome */
.welcome{height:388px;background:var(--orange);display:flex;align-items:center;padding:0 88px;gap:40px}
.welcome-photo{width:440px;height:248px;background:linear-gradient(135deg,#e8e4dd,#b9b1a5 60%,#8a8070);flex:none}
.welcome-text{color:var(--white)}
.welcome-text h2{font-family:"Roboto Condensed",sans-serif;font-size:34px;font-weight:700;text-transform:uppercase}
.welcome-text p{font-size:14px;line-height:21px;margin-top:14px;max-width:560px}
.btn-dark{display:inline-block;background:#3a3a3a;color:var(--white);font-size:13px;text-transform:uppercase;padding:10px 20px;margin-top:18px}

/* services */
.services{height:490px;text-align:center;padding-top:64px}
.services .section-title{color:var(--orange)}
.section-sub{font-size:15px;color:var(--muted);margin-top:10px}
.service-grid{display:flex;gap:10px;justify-content:center;margin-top:40px}
.service-card{width:250px}
.service-photo{height:210px}
.service-card figcaption{background:#f5f5f5;font-size:14px;font-weight:700;text-transform:uppercase;padding:14px 0;color:var(--ink)}

/* contact */
.quick-contact{position:relative;height:380px;margin-top:10px;background:linear-gradient(90deg,#4a4a3c 0%,#6f6a55 35%,#3b3a33 60%,#2b2b28 100%)}
.contact-form{position:absolute;left:520px;top:60px;width:592px}
.contact-form h2{font-family:"Roboto Condensed",sans-serif;font-size:30px;color:var(--white);text-transform:uppercase;font-weight:400;margin-bottom:18px}
.form-grid{display:grid;grid-template-columns:1fr 1fr;gap:12px 14px}
.field{background:var(--white);height:42px;font-size:14px;color:#888;padding:12px}
.field.tall{grid-row:span 2;height:96px}
.field.select{display:flex;justify-content:space-between}
.btn-submit{display:inline-block;background:var(--orange);color:var(--white);font-size:15px;font-weight:700;text-transform:uppercase;padding:12px 28px;margin-top:14px}

/* blog */
.blog{height:300px;padding:50px 88px 0}
.blog-head{display:flex;justify-content:space-between;align-items:center}
.blog-head h2{font-family:"Roboto Condensed",sans-serif;font-size:28px;font-weight:700;text-transform:uppercase}
.blog-head h2 em{font-style:normal;color:var(--orange)}
.blog-nav{font-size:28px;color:var(--ink);letter-spacing:6px}
.blog-list{display:flex;gap:40px;margin-top:30px}
.blog-item{display:flex;gap:22px;width:492px}
.blog-photo{width:172px;height:140px;flex:none}
.blog-item h3{font-size:15px;font-weight:500}
.blog-item time{display:block;font-size:12px;color:var(--muted);margin-top:6px}
.blog-item p{font-size:13px;color:var(--muted);line-height:18px;margin-top:8px}
.blog-item .more{font-size:13px;color:var(--orange);margin-top:6px;display:block}

/* footer */
.site-footer{height:280px;background:var(--footer);color:#cfcfcf;display:flex;padding:40px 88px 0;gap:40px}
.footer-col{flex:1}
.footer-col h4{color:var(--white);font-size:16px;font-weight:500;text-transform:uppercase;margin-bottom:18px}
.footer-col p,.footer-col li{font-size:13px;line-height:21px;list-style:none}
.footer-col li{display:flex;gap:10px;margin-bottom:6px}
.footer-col li i{width:12px;height:12px;background:var(--orange);flex:none;margin-top:4px}
.news-form{display:flex;margin-top:16px}
.news-form span{flex:1;background:var(--white);color:#999;font-size:12px;padding:10px 8px;white-space:nowrap;overflow:hidden}
.news-form b{background:var(--orange);color:var(--white);font-size:13px;padding:10px 14px;font-weight:500;white-space:nowrap}
.social-squares{display:flex;gap:10px}
.social-squares span{width:36px;height:36px;background:#3d3d3d;display:block}
.footer-bottom{height:44px;background:var(--footer-bottom);color:#999;font-size:13px;text-align:center;line-height:44px}
</style>
</head>
<body>

<header class="site-header">
  <div class="brand"><span class="brand-mark"></span><span class="brand-name">Lead Harbor</span></div>
  <div class="header-right">
    <div class="social-row"><span></span><span></span><span></span><span></span><span></span></div>
    <div class="contact-lines">
      <div class="phone">555-010-2468</div>
      <div>info@leadharbor.example</div>
    </div>
  </div>
</header>

<section class="hero">
  <div role="img" aria-label="Photo of a large suburban family home at dusk" style="position:absolute;inset:0"></div>
  <nav class="main-nav">
    <a class="active" href="#">Home</a>
    <a class="orange" href="#">About</a>
    <a class="orange" href="#">Services</a>
    <a class="orange" href="#">Projects</a>
    <a class="orange" href="#">Contact Us</a>
    <div class="nav-search">Search
      <svg width="14" height="14" viewBox="0 0 14 14"><circle cx="6" cy="6" r="4.5" fill="none" stroke="#666" stroke-width="1.6"/><line x1="9.5" y1="9.5" x2="13" y2="13" stroke="#666" stroke-width="1.6"/></svg>
    </div>
  </nav>
  <div class="hero-content">
    <div class="hero-mark"></div>
    <h1 class="hero-title">LEAD HARBOR</h1>
    <p class="hero-sub">Neque porro quisquam est qui dolorem</p>
  </div>
  <div class="hero-dots"><span class="on"></span><span></span><span></span><span></span><span></span></div>
</section>

<section class="process">
  <h2 class="section-title">Our 3Step <em>Process</em></h2>
  <div class="steps">
    <div class="step">
      <div class="step-icon"><svg width="40" height="40" viewBox="0 0 40 40"><circle cx="20" cy="20" r="9" fill="none" stroke="#f47b20" stroke-width="5" stroke-dasharray="5 2.5"/><circle cx="20" cy="20" r="3.5" fill="#f47b20"/></svg></div>
      <h3>STEP 1</h3>
      <p>Receive leads of the most recent New Movers in their area.</p>
    </div>
    <div class="step-arrow"><svg width="34" height="22" viewBox="0 0 34 22"><path d="M2 18 Q10 4 24 8 L22 2 L32 10 L22 17 L24 12 Q12 9 2 18Z" fill="#c9c9c9"/></svg></div>
    <div class="step">
      <div class="step-icon"><svg width="40" height="40" viewBox="0 0 40 40"><rect x="6" y="10" width="28" height="20" rx="2" fill="none" stroke="#f47b20" stroke-width="3"/><path d="M6 12 L20 22 L34 12" fill="none" stroke="#f47b20" stroke-width="3"/></svg></div>
      <h3>STEP 2</h3>
      <p>Do direct marketing of their company's services/products to those New Movers.</p>
    </div>
    <div class="step-arrow"><svg width="34" height="22" viewBox="0 0 34 22"><path d="M2 18 Q10 4 24 8 L22 2 L32 10 L22 17 L24 12 Q12 9 2 18Z" fill="#c9c9c9"/></svg></div>
    <div class="step">
      <div class="step-icon"><svg width="40" height="40" viewBox="0 0 40 40"><path d="M6 20 L20 7 L34 20 M11 16 V33 H29 V16" fill="none" stroke="#f47b20" stroke-width="3"/><rect x="17" y="23" width="6" height="10" fill="#f47b20"/></svg></div>
      <h3>STEP 3</h3>
      <p>If feel these leads/lists are not fresh and accurate, no obligation to pay. The leads are FREE.</p>
    </div>
  </div>
</section>

<section class="welcome">
  <div class="welcome-photo" role="img" aria-label="Photo of a bright modern living room with sofa and red accents"></div>
  <div class="welcome-text">
    <h2>Welcome to Lead Harbor</h2>
    <p>We supply fresh lists of residential new movers to local businesses that want to reach homeowners first. Each list is gathered from recent home sales, checked for accuracy and sorted by area so your mailing or calling campaign starts with the right people. Whether you install floors, fix plumbing or sell furniture, new homeowners need your services right now, and our lists help you meet them before anyone else does.</p>
    <a class="btn-dark" href="#">Read More</a>
  </div>
</section>

<section class="services">
  <h2 class="section-title">Services</h2>
  <p class="section-sub">Neque porro quisquam est qui dolorem ipsum quia dolor sit amet.</p>
  <div class="service-grid">
    <figure class="service-card"><div class="service-photo" role="img" aria-label="Photo of a bright room with new carpeting" style="background:linear-gradient(160deg,#f1efe9,#cfc8bb)"></div><figcaption>Carpeting/Flooring</figcaption></figure>
    <figure class="service-card"><div class="service-photo" role="img" aria-label="Photo of a house with a landscaped green lawn" style="background:linear-gradient(180deg,#8fb2d6 0%,#a99d88 45%,#5f8a3c 75%,#4a7a2c)"></div><figcaption>Residential Landscaping</figcaption></figure>
    <figure class="service-card"><div class="service-photo" role="img" aria-label="Photo of a remodeled kitchen interior" style="background:linear-gradient(160deg,#c98b4e,#8f5a2e 60%,#e9ddc8)"></div><figcaption>Home Remodeling</figcaption></figure>
    <figure class="service-card"><div class="service-photo" role="img" aria-label="Photo of hands repairing a sink pipe" style="background:linear-gradient(160deg,#f3f3f3,#cfd3d6 60%,#9aa0a5)"></div><figcaption>Plumbing</figcaption></figure>
  </div>
</section>

<section class="quick-contact">
  <div role="img" aria-label="Photo of a two-storey suburban home with front lawn" style="position:absolute;inset:0"></div>
  <form class="contact-form">
    <h2>Quick Contact</h2>
    <div class="form-grid">
      <div class="field">Name</div>
      <div class="field">Business Name</div>
      <div class="field">Email to Receive Lead</div>
      <div class="field tall">Comments/Questions</div>
      <div class="field select">Industry <svg width="10" height="8" viewBox="0 0 10 8"><path d="M0 0 H10 L5 7Z" fill="#888"/></svg></div>
    </div>
    <span class="btn-submit">Submit</span>
  </form>
</section>

<section class="blog">
  <div class="blog-head">
    <h2>Latest <em>Blog</em></h2>
    <span class="blog-nav">‹›</span>
  </div>
  <div class="blog-list">
    <article class="blog-item">
      <div class="blog-photo" role="img" aria-label="Photo of a furnished living room" style="background:linear-gradient(160deg,#e6dfd2,#a8957a)"></div>
      <div>
        <h3>Neme Enim Ipsam Volup</h3>
        <time>08.07.2016</time>
        <p>New homeowners make most buying choices in the first months. Reach them early with a clear offer and a friendly call.</p>
        <a class="more" href="#">Read More »</a>
      </div>
    </article>
    <article class="blog-item">
      <div class="blog-photo" role="img" aria-label="Photo of a modern kitchen" style="background:linear-gradient(160deg,#d9d4cb,#6d6357)"></div>
      <div>
        <h3>Neme Enim Ipsam Volup</h3>
        <time>08.07.2016</time>
        <p>A simple postcard sent in the first week can bring new customers. Keep the message short and the offer local.</p>
        <a class="more" href="#">Read More »</a>
      </div>
    </article>
  </div>
</section>

<footer>
  <div class="site-footer">
    <div class="footer-col">
      <h4>Contact Us</h4>
      <ul>
        <li><i></i>Unit 4, 210 Maple Row, Fairview</li>
        <li><i></i>555-013-5790</li>
        <li><i></i>info@leadharbor.example</li>
      </ul>
    </div>
    <div class="footer-col">
      <h4>Latest Tweets</h4>
      <ul>
        <li><i></i><p>Fresh new mover lists are ready for this week. Ask about your area and get started today with free leads. @leadharbor</p></li>
      </ul>
    </div>
    <div class="footer-col">
      <h4>Newsletter</h4>
      <p>Subscribe to our newsletter for tips on reaching new homeowners and updates on fresh lists.</p>
      <div class="news-form"><span>Enter your email</span><b>Sign Up</b></div>
    </div>
    <div class="footer-col">
      <h4>Social Media</h4>
      <div class="social-squares"><span></span><span></span><span></span></div>
    </div>
  </div>
  <div class="footer-bottom">2016. All Rights Reserved.</div>
</footer>

</body>
</html>
```